Pellham Ridge Nectar Company, local Honey producer needs product Lable to encourage sales

We are a small business (Pellham Ridge Nectar Company) located in a small Texas town that harvests honey from our beehives yearly. Our honey would be considered "raw wildflower honey" and our goal is to sell it locally (farmers markets) and to surrounding areas.

We are currently packaging in plastic classic honey bottles with white flip caps. Sizes are 8oz and 16oz bottles (see pictures for actual size). Larger orders will be filled in one quart mason jars.

Design Ideas:
-vintage style design with bee or several bees in background
- incorporate company name "Pellham Ridge Nectar Company"
- needs small description "Raw Honey", and "Harvested in Cedarholt, Texas"

Target Market(s)

Farmers markets, health conscience people looking for unprocessed food options

Industry/Entity Type

Small Business

Requirements
Nice to have
• Vintage feel
Should not have
• No cartoonish characters

```html
<!DOCTYPE html>
<html lang="en">
<head>
<meta charset="utf-8">
<title>Pellham Ridge Nectar Company – Raw Honey Label</title>
<link href="https://fonts.googleapis.com/css2?family=Dancing+Script:wght@600;700&family=Kaushan+Script&family=Libre+Baskerville&display=swap" rel="stylesheet">
<style>
  :root {
    --backdrop: #f1ede4;
    --label-cream: #eee7cf;
    --label-edge: #3b2a12;
    --gold: #d6a11f;
    --gold-deep: #a8770e;
    --gold-light: #ecc95a;
    --ink: #1d1a14;
    --ribbon: #fbfaf5;
    --ribbon-shade: #d9d5c8;
    --ribbon-fold: #a9a496;
    --meadow-green: #a7b27c;
    --meadow-yellow: #e6cf63;
    --meadow-pink: #d9a3a8;
    --meadow-violet: #b3a0c9;
  }
  html, body {
    margin: 0;
    padding: 0;
    width: 805px;
    height: 1200px;
    overflow: hidden;
    background: var(--backdrop);
  }
  .canvas {
    position: relative;
    width: 805px;
    height: 1200px;
  }
  .label {
    position: absolute;
    left: 62px;
    top: 50px;
    width: 681px;
    height: 1100px;
    box-sizing: border-box;
    border-radius: 50%;
    background: var(--label-cream);
    border: 4px solid var(--label-edge);
    box-shadow: inset 0 0 0 16px var(--gold), inset 0 0 0 19px var(--label-edge);
  }
  .brand-banner {
    position: absolute;
    left: 190px;
    top: 110px;
    width: 300px;
    height: 150px;
  }
  .brand-banner svg { position: absolute; inset: 0; }
  .brand-name {
    position: absolute;
    inset: 18px 10px 28px;
    margin: 0;
    display: flex;
    align-items: center;
    justify-content: center;
    text-align: center;
    font-family: "Dancing Script", cursive;
    font-weight: 700;
    font-size: 40px;
    line-height: 1.05;
    color: var(--ink);
  }
  .product-title {
    position: absolute;
    left: 0;
    right: 0;
    top: 275px;
    margin: 0;
    text-align: center;
    font-family: "Kaushan Script", cursive;
    font-weight: 400;
    font-size: 104px;
    line-height: 1;
    color: var(--gold);
    white-space: nowrap;
  }
  .product-title .bee-mark {
    display: inline-block;
    width: 58px;
    height: 40px;
    margin: 0 10px;
    vertical-align: 44px;
    border-radius: 50%;
    background: linear-gradient(180deg, var(--gold-light) 0%, var(--gold) 60%, var(--gold-deep) 100%);
  }
  .wildflowers {
    position: absolute;
    left: 115px;
    top: 420px;
    width: 450px;
    height: 285px;
    border-radius: 28px;
    background:
      linear-gradient(180deg, rgba(238,231,207,0) 55%, var(--meadow-green) 100%),
      linear-gradient(90deg, var(--meadow-pink) 0%, var(--meadow-yellow) 35%, var(--meadow-yellow) 60%, var(--meadow-violet) 100%);
    opacity: 0.85;
  }
  .origin-ribbon {
    position: absolute;
    left: 40px;
    top: 720px;
    width: 600px;
    height: 96px;
  }
  .origin-ribbon svg { position: absolute; inset: 0; }
  .origin-text {
    position: absolute;
    left: 60px;
    right: 60px;
    top: 14px;
    margin: 0;
    text-align: center;
    font-family: "Dancing Script", cursive;
    font-weight: 600;
    font-size: 38px;
    line-height: 48px;
    color: var(--ink);
    white-space: nowrap;
  }
  .bee-emblem {
    position: absolute;
    left: 255px;
    top: 840px;
    width: 170px;
    height: 105px;
    border-radius: 50%;
    background: linear-gradient(180deg, var(--gold-light) 0%, var(--gold) 55%, var(--gold-deep) 100%);
  }
  .net-weight {
    position: absolute;
    left: 0;
    right: 0;
    top: 970px;
    margin: 0;
    text-align: center;
    font-family: "Libre Baskerville", serif;
    font-size: 30px;
    color: var(--ink);
  }
</style>
</head>
<body>
<main class="canvas">
  <section class="label">
    <div class="brand-banner">
      <svg viewBox="0 0 300 150" width="300" height="150" aria-hidden="true">
        <polygon points="6,4 294,4 294,128 150,146 6,128" fill="var(--ribbon)" stroke="var(--ribbon-shade)" stroke-width="3"/>
      </svg>
      <h1 class="brand-name">Pellham Ridge Nectar Company</h1>
    </div>

    <h2 class="product-title">Raw<span class="bee-mark" role="img" aria-label="Small gold vintage bee illustration"></span>Honey</h2>

    <div class="wildflowers" role="img" aria-label="Vintage illustration of Texas wildflowers in yellow, pink and purple"></div>

    <div class="origin-ribbon">
      <svg viewBox="0 0 600 96" width="600" height="96" aria-hidden="true">
        <polygon points="0,30 60,30 60,88 0,88 22,59" fill="var(--ribbon-shade)"/>
        <polygon points="600,30 540,30 540,88 600,88 578,59" fill="var(--ribbon-shade)"/>
        <rect x="50" y="6" width="500" height="68" fill="var(--ribbon)" stroke="var(--ribbon-shade)" stroke-width="3"/>
        <polygon points="50,74 60,88 60,74" fill="var(--ribbon-fold)"/>
        <polygon points="550,74 540,88 540,74" fill="var(--ribbon-fold)"/>
      </svg>
      <p class="origin-text">Harvested in Cedarholt, Texas</p>
    </div>

    <div class="bee-emblem" role="img" aria-label="Gold vintage honeybee illustration"></div>

    <p class="net-weight">16oz</p>
  </section>
</main>
</body>
</html>
```